New Product Design

We want to develop new Wafer Biscuits Product design of Vanilla / strawberry / choclate flavour. Designer can design first any of the flavour ( Vanilla/Chcolate/Starwberry). Based on the first any variety design will go for other designs.
Wafer is in finger form .
Name of the Brand will be TOBI LUN
Wafer fingre (sample pics and TOBI LUN brand image is attached in word file for reference.

Smaple pics of the fingre is attached for ref.

Target Market(s)

Children and Youth

Industry/Entity Type

Food

```html
<!DOCTYPE html>
<html lang="en">
<head>
<meta charset="UTF-8">
<title>TOBI LUN Wafers – Vanilla &amp; Strawberry</title>
<link rel="stylesheet" href="https://fonts.googleapis.com/css2?family=Bowlby+One&family=Montserrat:wght@500&family=Dancing+Script:wght@500&display=swap">
<style>
  :root {
    --page: #ffffff;
    --vanilla-deep: #0b2f9e;
    --vanilla-mid: #1f63c8;
    --vanilla-light: #4fa0e2;
    --straw-yellow: #f3d21c;
    --straw-orange: #f2a524;
    --straw-pink: #e8246e;
    --white: #ffffff;
    --silver: #e9eaec;
    --ink: #141414;
    --vanilla-script: #1128a8;
    --straw-script: #e0309e;
    --wafer-light: #f1d99a;
    --wafer-dark: #c99a4e;
    --cream: #f7f1e2;
  }
  * { margin: 0; padding: 0; box-sizing: border-box; }
  html, body {
    width: 1200px;
    height: 1200px;
    overflow: hidden;
    background: var(--page);
  }
  .canvas {
    position: relative;
    width: 1200px;
    height: 1200px;
  }
  .pack {
    position: absolute;
    left: 80px;
    width: 1030px;
    height: 430px;
    border-radius: 10px;
    overflow: hidden;
    box-shadow: 0 14px 30px rgba(0, 0, 0, 0.12);
  }
  .pack--vanilla { top: 141px; }
  .pack--strawberry { top: 629px; }
  .pack__art {
    position: absolute;
    inset: 0;
    width: 100%;
    height: 100%;
  }
  .brand-name {
    position: absolute;
    left: 168px;
    top: 58px;
    width: 320px;
    font-family: "Bowlby One", "Arial Black", sans-serif;
    font-size: 108px;
    line-height: 1.08;
    color: var(--white);
    letter-spacing: 1px;
    white-space: nowrap;
  }
  .product-type {
    position: absolute;
    left: 308px;
    top: 348px;
    font-family: "Montserrat", Arial, sans-serif;
    font-weight: 500;
    font-size: 30px;
    letter-spacing: 1px;
    color: var(--ink);
  }
  .product-photo {
    position: absolute;
    left: 535px;
    top: 82px;
    width: 425px;
    height: 215px;
    border-radius: 14px;
    background: linear-gradient(160deg, var(--wafer-light) 0%, var(--cream) 55%, var(--wafer-dark) 100%);
  }
  .flavour {
    position: absolute;
    font-family: "Dancing Script", cursive;
    font-weight: 500;
    font-size: 52px;
    line-height: 1;
    transform: rotate(-8deg);
    transform-origin: left bottom;
    white-space: nowrap;
  }
  .flavour--vanilla {
    left: 650px;
    top: 330px;
    color: var(--vanilla-script);
  }
  .flavour--strawberry {
    left: 650px;
    top: 330px;
    color: var(--straw-script);
  }
</style>
</head>
<body>
<main class="canvas">

  <section class="pack pack--vanilla" aria-label="TOBI LUN wafers, vanilla flavour pack">
    <svg class="pack__art" viewBox="0 0 1030 430" preserveAspectRatio="none" aria-hidden="true">
      <defs>
        <linearGradient id="vanilla-sky" x1="0" y1="0" x2="1" y2="0">
          <stop offset="0" stop-color="var(--vanilla-deep)"/>
          <stop offset="0.5" stop-color="var(--vanilla-mid)"/>
          <stop offset="0.85" stop-color="var(--vanilla-light)"/>
          <stop offset="1" stop-color="var(--vanilla-mid)"/>
        </linearGradient>
      </defs>
      <rect class="pack__colour" width="1030" height="430" fill="url(#vanilla-sky)"/>
      <path class="pack__swoosh" d="M0,210 C80,310 220,345 420,340 C620,335 800,300 1000,240 L1000,430 L0,430 Z" fill="var(--white)"/>
      <path class="pack__splash" d="M540,110 C560,55 630,40 690,70 C750,30 850,25 920,60 C975,85 990,140 975,200 L975,300 C880,320 720,320 560,300 C525,250 520,170 540,110 Z" fill="var(--white)" opacity="0.9"/>
      <rect class="pack__seal pack__seal--left" x="0" y="0" width="28" height="430" fill="var(--silver)" opacity="0.5"/>
      <rect class="pack__seal pack__seal--right" x="1002" y="0" width="28" height="430" fill="var(--silver)" opacity="0.5"/>
    </svg>
    <div class="brand-name">TOBI<br>LUN</div>
    <div class="product-type">WAFERS</div>
    <div class="product-photo" role="img" aria-label="Photo of a stacked vanilla cream wafer with cream filling"></div>
    <div class="flavour flavour--vanilla">Vanilla Flavour</div>
  </section>

  <section class="pack pack--strawberry" aria-label="TOBI LUN wafers, strawberry flavour pack">
    <svg class="pack__art" viewBox="0 0 1030 430" preserveAspectRatio="none" aria-hidden="true">
      <defs>
        <linearGradient id="straw-sky" x1="0" y1="0" x2="1" y2="0">
          <stop offset="0" stop-color="var(--straw-yellow)"/>
          <stop offset="0.5" stop-color="var(--straw-orange)"/>
          <stop offset="0.82" stop-color="var(--straw-orange)"/>
          <stop offset="1" stop-color="var(--straw-pink)"/>
        </linearGradient>
      </defs>
      <rect class="pack__colour" width="1030" height="430" fill="url(#straw-sky)"/>
      <path class="pack__swoosh" d="M0,210 C80,310 220,345 420,340 C620,335 800,300 1000,240 L1000,430 L0,430 Z" fill="var(--white)"/>
      <path class="pack__splash" d="M540,110 C560,55 630,40 690,70 C750,30 850,25 920,60 C975,85 990,140 975,200 L975,300 C880,320 720,320 560,300 C525,250 520,170 540,110 Z" fill="var(--white)" opacity="0.9"/>
      <rect class="pack__seal pack__seal--left" x="0" y="0" width="28" height="430" fill="var(--silver)" opacity="0.5"/>
      <rect class="pack__seal pack__seal--right" x="1002" y="0" width="28" height="430" fill="var(--silver)" opacity="0.5"/>
    </svg>
    <div class="brand-name">TOBI<br>LUN</div>
    <div class="product-type">WAFERS</div>
    <div class="product-photo" role="img" aria-label="Photo of a stacked strawberry cream wafer with cream filling"></div>
    <div class="flavour flavour--strawberry">Strawberry</div>
  </section>

</main>
</body>
</html>
```